Residential & commercial cleaning business

Looking for Brazilian colors, green/blue/yellow.
Name of business is “Marta’s Cleaning”.
Second side of card will be for ‘confirming customer next appointment date/time.
Want to include in description…residential & commercial cleaning, experienced, highly recommended, reasonable rates, free estimates, Marta’sCleaningNH@brightmail.example, Cedarford, NH, Call today at 603.555.0148.

```html
<!DOCTYPE html>
<html lang="en">
<head>
<meta charset="utf-8">
<title>Marta’s Cleaning – Business Card</title>
<link rel="stylesheet" href="https://fonts.googleapis.com/css2?family=Poppins:wght@400;600;700&display=swap">
<style>
  :root {
    --green: #05a03a;
    --yellow: #ffe000;
    --white: #ffffff;
    --ink: #2f2f2f;
    --backdrop: #1f1f1f;
  }
  * { box-sizing: border-box; margin: 0; padding: 0; }
  html, body { width: 1200px; height: 1200px; overflow: hidden; }
  body {
    background: var(--backdrop);
    font-family: "Poppins", sans-serif;
    color: var(--ink);
    position: relative;
  }
  .card {
    position: absolute;
    left: 120px;
    width: 960px;
    height: 530px;
    overflow: hidden;
    background: var(--white);
  }
  .card--front { top: 50px; }
  .card--back { top: 620px; }

  .band {
    position: absolute;
    left: 0; right: 0;
    height: 56px;
    background: var(--green);
  }
  .band::after {
    content: "";
    position: absolute;
    left: 0; right: 0;
    height: 14px;
    background: var(--yellow);
  }
  .band--bottom { bottom: 0; }
  .band--bottom::after { bottom: 0; }
  .band--top { top: 0; }
  .band--top::after { top: 0; }

  .brand-name {
    position: absolute;
    font-weight: 700;
    color: var(--green);
    line-height: 1.05;
  }
  .card--front .brand-name { left: 80px; top: 150px; font-size: 50px; }
  .card--back .brand-name { left: 70px; top: 150px; font-size: 50px; }

  .divider {
    position: absolute;
    left: 440px; top: 120px;
    width: 2px; height: 170px;
    background: var(--green);
  }
  .contact {
    position: absolute;
    left: 480px; top: 132px;
  }
  .contact__title {
    font-size: 21px; font-weight: 600; letter-spacing: 1px;
    margin-bottom: 22px;
  }
  .contact__list { list-style: none; }
  .contact__item {
    display: flex; align-items: center; gap: 12px;
    font-size: 19px; line-height: 1.6;
  }
  .contact__icon {
    width: 24px; height: 24px; border-radius: 50%;
    background: var(--green);
    display: flex; align-items: center; justify-content: center;
    flex: none;
  }

  .services {
    position: absolute;
    right: 70px; top: 110px;
    text-align: right;
  }
  .services__title {
    font-size: 23px; font-weight: 700; color: var(--green);
    letter-spacing: 1px; margin-bottom: 6px;
  }
  .services__list { list-style: none; }
  .services__item {
    display: flex; justify-content: flex-end; align-items: center; gap: 12px;
    font-size: 24px; line-height: 1.4;
  }
  .services__dot {
    width: 10px; height: 10px; border-radius: 50%;
    background: var(--yellow); flex: none;
  }

  .appointment {
    position: absolute;
    left: 280px; right: 70px; top: 390px;
  }
  .appointment__title {
    text-align: right;
    font-size: 24px; font-weight: 700; color: var(--green);
    letter-spacing: 1px;
  }
  .appointment__line {
    display: flex; align-items: flex-end; gap: 8px;
    font-size: 24px; margin-top: 10px;
  }
  .appointment__fill {
    flex: 1; border-bottom: 3px dotted var(--ink); height: 1px; margin-bottom: 8px;
  }
</style>
</head>
<body>

<section class="card card--front">
  <div class="band band--bottom" aria-hidden="true"></div>

  <div class="brand-name">Marta’s<br>Cleaning</div>
  <div class="divider"></div>

  <div class="contact">
    <h2 class="contact__title">MARTA’S CLEANING</h2>
    <ul class="contact__list">
      <li class="contact__item">
        <span class="contact__icon">
          <svg width="14" height="14" viewBox="0 0 24 24"><path fill="#fff" d="M6.6 10.8a15 15 0 0 0 6.6 6.6l2.2-2.2c.3-.3.7-.4 1-.2 1.1.4 2.3.6 3.6.6.6 0 1 .4 1 1V20c0 .6-.4 1-1 1A17 17 0 0 1 3 4c0-.6.4-1 1-1h3.5c.6 0 1 .4 1 1 0 1.3.2 2.5.6 3.6.1.3 0 .7-.2 1z"/></svg>
        </span>
        603.555.0148
      </li>
      <li class="contact__item">
        <span class="contact__icon">
          <svg width="14" height="14" viewBox="0 0 24 24"><rect x="2" y="5" width="20" height="14" rx="2" fill="#fff"/><path d="M3 6l9 7 9-7" stroke="#05a03a" stroke-width="2" fill="none"/></svg>
        </span>
        Marta’sCleaningNH@brightmail.example
      </li>
      <li class="contact__item">
        <span class="contact__icon">
          <svg width="14" height="14" viewBox="0 0 24 24"><path fill="#fff" d="M12 2a7 7 0 0 0-7 7c0 5 7 13 7 13s7-8 7-13a7 7 0 0 0-7-7zm0 9.5A2.5 2.5 0 1 1 12 6.5a2.5 2.5 0 0 1 0 5z"/></svg>
        </span>
        Cedarford, NH
      </li>
    </ul>
  </div>
</section>

<section class="card card--back">
  <div class="band band--top" aria-hidden="true"></div>

  <div class="brand-name">Marta’s<br>Cleaning</div>

  <div class="services">
    <h2 class="services__title">OUR SERVICES</h2>
    <ul class="services__list">
      <li class="services__item">residential &amp; commercial cleaning<span class="services__dot"></span></li>
      <li class="services__item">experienced<span class="services__dot"></span></li>
      <li class="services__item">highly recommended<span class="services__dot"></span></li>
      <li class="services__item">reasonable rates<span class="services__dot"></span></li>
      <li class="services__item">free estimates<span class="services__dot"></span></li>
    </ul>
  </div>

  <div class="appointment">
    <h3 class="appointment__title">NEXT APPOINTMENT</h3>
    <div class="appointment__line"><span class="appointment__fill"></span></div>
    <div class="appointment__line">
      <span class="appointment__fill"></span>AT<span class="appointment__fill"></span>AM/PM
    </div>
  </div>
</section>

</body>
</html>
```